Church needs an introductory/informative postcard

We are looking for a postcard that would introduce our church along with having our programing information. We need it to be in Spanish, I can provide the necessary translation. Please provide us with ideas for a tag line that invites people to come check us out. We can provide a bible scripture if necessary, but would like something short that projects interest and confidence. We have a logo that we would like incorporated.

Target Market(s)

Hispanic

Industry/Entity Type

Religious

Requirements
Must have
• Colorful to coordinate with our logo so it flows well
• Have an tag line that invites people to our church
Nice to have
• have a modern feel
• if needed we can provide some pictures of our building
Should not have
• Pictures of people

```html
<!DOCTYPE html>
<html lang="es">
<head>
<meta charset="utf-8">
<title>Postal Iglesia de Dios Betania</title>
<link href="https://fonts.googleapis.com/css2?family=Lobster&family=Montserrat:wght@400;500;700&family=Oswald:wght@600&display=swap" rel="stylesheet">
<style>
  :root {
    --bg: #b9b9b9;
    --sky-pink: #f2cfc9;
    --sky-blue: #7cc6dc;
    --sun: #f7d79a;
    --stone: #a8795a;
    --grass: #c9a64a;
    --field: #7f9a45;
    --headline: #2a9ddd;
    --headline-edge: #e0643a;
    --ink: #1d1d1d;
    --brand: #4b2a7f;
    --band: rgba(255, 255, 255, 0.72);
  }
  * { box-sizing: border-box; margin: 0; padding: 0; }
  html, body { width: 1200px; height: 800px; overflow: hidden; }
  body {
    background: var(--bg);
    font-family: "Montserrat", sans-serif;
    position: relative;
  }
  .postcard {
    position: absolute;
    top: 214px;
    width: 560px;
    height: 373px;
    overflow: hidden;
    box-shadow: 0 2px 6px rgba(0,0,0,0.25);
  }
  .postcard--front { left: 30px; }
  .postcard--back { left: 610px; }

  .scene-photo {
    position: absolute;
    inset: 0;
    background:
      radial-gradient(circle at 62% 42%, var(--sun) 0%, rgba(247,215,154,0) 28%),
      linear-gradient(180deg, var(--sky-pink) 0%, #f5ddd2 30%, var(--sky-blue) 44%, #e9c9a8 52%, var(--stone) 62%, var(--grass) 74%, var(--field) 86%, #d8cfc2 100%);
  }
  .postcard--back .scene-photo { opacity: 0.32; }

  .headline {
    position: absolute;
    right: 40px;
    top: 20px;
    font-family: "Lobster", cursive;
    font-weight: 400;
    font-size: 66px;
    line-height: 1.05;
    color: var(--headline);
    text-align: center;
    text-shadow: 1px 1px 0 var(--headline-edge);
  }
  .info-band {
    position: absolute;
    left: 0; right: 0; bottom: 0;
    height: 108px;
    background: var(--band);
  }
  .info-band__text {
    position: absolute;
    right: 22px;
    top: 20px;
    font-size: 15.5px;
    line-height: 1.3;
    color: var(--ink);
    text-align: right;
  }
  .brand {
    position: absolute;
    left: 24px;
    bottom: 22px;
    display: flex;
    align-items: center;
    gap: 8px;
    font-weight: 700;
    font-size: 17px;
    letter-spacing: 1px;
    color: var(--brand);
    text-transform: uppercase;
  }
  .brand__dot {
    width: 26px; height: 26px;
    border-radius: 50%;
    background: var(--brand);
  }

  .schedule {
    position: absolute;
    left: 290px;
    top: 88px;
    max-width: 250px;
    padding-left: 12px;
    border-left: 2px solid var(--ink);
    font-size: 18px;
    line-height: 1.22;
    color: var(--ink);
    white-space: nowrap;
  }
  .schedule__title { font-weight: 700; }
  .web-address {
    position: absolute;
    left: 0; right: 0;
    bottom: 20px;
    text-align: center;
    font-family: "Oswald", sans-serif;
    font-weight: 600;
    font-size: 15px;
    letter-spacing: 0.5px;
    color: var(--brand);
    text-transform: uppercase;
  }
</style>
</head>
<body>
  <section class="postcard postcard--front">
    <div class="scene-photo" role="img" aria-label="Capilla de piedra junto a un lago con cruz de madera, montañas y cielo al atardecer"></div>
    <h1 class="headline">Demo<br>Text</h1>
    <div class="info-band">
      <p class="info-band__text">Demo text Demo text Demo text<br>Demo text Demo text Demo text</p>
    </div>
    <div class="brand"><span class="brand__dot"></span>Betania</div>
  </section>

  <section class="postcard postcard--back">
    <div class="scene-photo" role="img" aria-label="Capilla de piedra junto a un lago, en tono suave y desvanecido"></div>
    <div class="schedule">
      <p class="schedule__title">Servicios:</p>
      <p>Domingo 10:00 am</p>
      <p>Lunes 7:00 pm</p>
      <p>Miércoles 7:00 pm</p>
      <p>Iglesia de Dios<br>Betania</p>
      <p>482 Alder Ridge St.</p>
      <p>Cedar Hollow, TX 75999</p>
    </div>
    <p class="web-address">www.iglesiadediosbetania.org</p>
  </section>
</body>
</html>
```